Vale Lanternwick Needs a new website!

We need a four page website for a new company based in San Francisco. We help companies connect better with their clients, employees, and vendors by implementing collaborative technology.
Similar Websites
Brindle Oarsmen - http://www.brindleoarsmen.example/
Mossquill - http://www.mossquill.example/ - I don't like the the rotating window or the pictures of people. I like the icons used to go to the next pages.
Color Combos
Blues and Yellows - http://www.huepairings.example/hue-sets/96/HueSet96.html
We prefer graphics over the actual pictures of people in the header. Pictures of people working together in the text is fine.
Web Page Layout
Index
Cloud Advisory Services
Email Everywhere
CRM Implementation
For detailed copy please see this link https://pages.fernlodge.example/a/tinkerwrensf.example/document/d/7KxTqP2mZvLw9RbHs4-_n-YcEuJdAoNfgXtVkQr5mwbe/edit
Industry/Entity Type
It Company

```html
<!DOCTYPE html>
<html lang="en">
<head>
<meta charset="utf-8">
<title>Vale Lanternwick</title>
<link rel="stylesheet" href="https://fonts.googleapis.com/css2?family=Questrial&family=Noto+Sans:wght@400;700&display=swap">
<style>
:root{
  --blue:#2460b0;
  --blue-dark:#1d4f94;
  --blue-deep:#16407c;
  --yellow:#f2c200;
  --yellow-dark:#e0b000;
  --ink:#333;
  --grey:#8a8a8a;
  --line:#dcdcdc;
  --page:#f7f7f7;
  --white:#fff;
  --bottom:#2b2b2b;
}
*{box-sizing:border-box;margin:0;padding:0}
html,body{width:1200px;height:3197px;overflow:hidden}
body{background:var(--page);font-family:"Noto Sans",Verdana,sans-serif;color:var(--ink);position:relative}
.abs{position:absolute}
.heading{font-family:"Questrial",sans-serif}

/* top bar */
.topbar{left:0;top:0;width:1200px;height:30px;background:var(--blue)}
.topbar .contact{left:160px;top:7px;color:#fff;font-size:11px;display:flex;gap:26px;align-items:center}
.topbar .contact span{display:flex;align-items:center;gap:6px}
.social-dots{display:flex;gap:5px}
.social-dots i{display:block;width:15px;height:15px;border-radius:50%;background:#fff}
.topbar .social-dots{position:absolute;left:987px;top:7px}

/* header */
.header{left:0;top:30px;width:1200px;height:140px;background:var(--page)}
.brand{left:140px;top:52px;display:flex;align-items:center;gap:10px}
.brand .mark{width:36px;height:36px;border-radius:50%;background:var(--blue)}
.brand .name{font-family:"Questrial",sans-serif;font-size:30px;color:var(--blue);font-weight:400}
.nav{left:517px;top:72px;display:flex;gap:33px;font-family:"Questrial",sans-serif;font-size:14px;color:#444;letter-spacing:.3px}
.header-rule{left:0;top:170px;width:1200px;height:5px;background:var(--yellow)}

/* hero */
.hero{left:0;top:175px;width:1200px;height:445px;overflow:hidden}
.hero-photo{position:absolute;inset:0;background:linear-gradient(100deg,#a9c7de 0%,#d6e5ee 35%,#eef2f4 55%,#b7cbd9 80%,#8eaac1 100%)}
.hero-clouds{position:absolute;left:0;top:335px}
.hero-card{left:141px;top:124px;width:388px}
.hero-card .title{height:52px;background:var(--blue-deep);color:#fff;font-family:"Questrial",sans-serif;font-size:33px;padding:6px 0 0 14px;position:relative;letter-spacing:.5px}
.hero-card .title .badge{position:absolute;right:0;top:0;width:78px;height:52px;background:var(--yellow);clip-path:polygon(22% 0,100% 0,100% 100%,0 100%)}
.hero-card .title .badge span{position:absolute;right:18px;top:9px;width:34px;height:34px;border-radius:50%;background:var(--blue-deep)}
.hero-card .body{background:rgba(36,96,176,.88);color:#fff;font-size:15px;line-height:25px;padding:6px 14px 10px}
.btn{display:inline-block;background:var(--yellow);color:#4a3a00;font-size:13px;text-align:center}
.hero-card .btn{position:absolute;left:0;top:358px;width:128px;height:34px;line-height:34px}
.dots{left:562px;top:601px;display:flex;gap:7px}
.dots i{width:11px;height:11px;border-radius:50%;background:#a8bfdc;display:block}
.dots i:first-child{background:var(--blue)}

/* section heads */
.section-title{width:1200px;left:0;text-align:center;font-size:25px;letter-spacing:.5px}
.section-title .a{color:var(--yellow)}
.section-title .b{color:var(--blue)}
.rule{left:158px;width:884px;height:1px;background:var(--line)}
.lead{left:180px;width:840px;text-align:center;font-size:15px;line-height:26px;color:var(--grey)}

/* feature cards */
.feature{top:916px;width:254px;height:426px;background:linear-gradient(#fff 0%,#fff 40%,#ececec 100%);border-bottom:5px solid #d3d3d3;box-shadow:0 1px 2px rgba(0,0,0,.08)}
.feature .ring{position:absolute;left:37px;top:-64px;width:180px;height:180px;border-radius:50%;background:#fff;border:4px solid #dedede;display:flex;align-items:center;justify-content:center}
.feature .ring span{width:160px;height:160px;border-radius:50%;background:var(--blue);display:flex;align-items:center;justify-content:center}
.feature h3{position:absolute;left:0;top:130px;width:100%;text-align:center;font-family:"Questrial",sans-serif;font-weight:400;font-size:20px;line-height:27px;color:#222;letter-spacing:.5px}
.feature p{position:absolute;left:22px;top:180px;width:210px;height:163px;overflow:hidden;text-align:center;font-size:13.5px;line-height:23px;color:#666}
.feature .btn{position:absolute;left:64px;top:358px;width:116px;height:32px;line-height:32px}

/* services */
.services{left:0;top:1428px;width:1200px;height:541px;background:var(--blue)}
.notch{left:585px;top:1428px;width:0;height:0;border-left:15px solid transparent;border-right:15px solid transparent;border-top:22px solid var(--page)}
.services .section-title .b{color:#fff}
.services .rule{background:#5a86c4}
.services .lead{color:#fff}
.service{width:170px;text-align:center;color:#fff;font-family:"Questrial",sans-serif;font-size:15px;line-height:19px;letter-spacing:.4px}
.service .icon{width:100px;height:100px;border-radius:50%;border:2px solid #fff;margin:0 auto 17px;display:flex;align-items:center;justify-content:center}
.services .btn{left:541px;top:458px;width:118px;height:36px;line-height:36px;position:absolute}

/* team */
.member{top:2272px;width:283px;height:441px;background:linear-gradient(#fff 0%,#fff 45%,#ececec 100%);border-bottom:5px solid #d3d3d3;box-shadow:0 1px 2px rgba(0,0,0,.08)}
.member .avatar{position:absolute;left:79px;top:-58px;width:124px;height:124px;border-radius:50%;border:5px solid var(--blue-deep)}
.member .avatar.a1{background:radial-gradient(circle at 50% 45%,#e0b79a 0%,#b98a6c 45%,#2d6b3a 100%)}
.member .avatar.a2{background:radial-gradient(circle at 50% 45%,#e9c9ae 0%,#c9a276 45%,#7fb0da 100%)}
.member h4{position:absolute;left:0;top:90px;width:100%;text-align:center;font-weight:400;font-size:15px;color:var(--blue)}
.member p{position:absolute;left:30px;top:118px;width:223px;height:216px;overflow:hidden;text-align:center;font-size:13px;line-height:23px;color:#666}
.member .pill{position:absolute;left:93px;top:356px;width:97px;height:28px;line-height:28px;border-radius:14px;background:var(--blue-dark);color:#fff;font-size:12.5px;text-align:center}
.member .social-dots{position:absolute;left:99px;top:402px;gap:6px}
.member .social-dots i{width:22px;height:22px;background:var(--blue)}

/* footer */
.footer{left:0;top:2792px;width:1200px;height:368px;background:var(--blue)}
.footer h5{position:absolute;top:70px;font-family:"Questrial",sans-serif;font-weight:400;font-size:16px;color:#fff;letter-spacing:.4px}
.footer ul{position:absolute;top:118px;list-style:none;color:#fff;font-size:12.5px;line-height:30px}
.footer ul li::before{content:"› ";font-weight:700}
.footer .contact-list{position:absolute;left:612px;top:118px;color:#fff;font-size:12.5px;line-height:30px}
.footer .social-dots{position:absolute;left:612px;top:185px;gap:8px}
.footer .social-dots i{width:22px;height:22px}
.field{position:absolute;left:850px;width:194px;background:#fff;font-size:11px;color:#999;padding:6px 8px}
.submit{position:absolute;left:850px;top:304px;width:87px;height:28px;line-height:28px;text-align:center;background:var(--blue-deep);color:#fff;font-size:11px;letter-spacing:.5px}
.copyright{left:0;top:3160px;width:1200px;height:37px;background:var(--bottom);color:#fff;font-size:12px;padding:11px 0 0 153px}
</style>
</head>
<body>

<div class="abs topbar">
  <div class="abs contact">
    <span><svg width="12" height="9" viewBox="0 0 12 9"><rect x="0.5" y="0.5" width="11" height="8" fill="none" stroke="#fff"/><path d="M0.5 0.5 6 5 11.5 0.5" fill="none" stroke="#fff"/></svg>hello@valelanternwick.example</span>
    <span><svg width="11" height="11" viewBox="0 0 11 11"><path d="M2 0h2l1 3-1.5 1a6 6 0 0 0 3.5 3.5L8 6l3 1v2a2 2 0 0 1-2 2A9 9 0 0 1 0 2a2 2 0 0 1 2-2z" fill="#fff"/></svg>02-5550-0147</span>
  </div>
  <div class="social-dots"><i></i><i></i><i></i></div>
</div>

<div class="abs header">
  <div class="abs brand"><span class="mark"></span><span class="name">Vale Lanternwick</span></div>
  <nav class="abs nav"><span>Cloud Services</span><span>Cloud Advisory</span><span>Cloud Technology</span><span>Case Studies</span></nav>
</div>
<div class="abs header-rule"></div>

<section class="abs hero">
  <div class="hero-photo" role="img" aria-label="Photo of two businessmen smiling and talking over a laptop in a bright office"></div>
  <svg class="hero-clouds" width="1200" height="110" viewBox="0 0 1200 110">
    <path d="M0 60 C30 30 70 40 90 60 C110 20 170 25 190 55 C220 30 260 45 270 65 C300 40 340 50 360 70 C380 60 400 62 420 72 L780 72 C800 60 830 55 850 65 C870 35 920 35 940 60 C960 30 1010 30 1030 58 C1050 25 1100 30 1120 55 C1140 35 1180 40 1200 50 L1200 110 L0 110 Z" fill="#f7f7f7"/>
  </svg>
  <div class="abs hero-card">
    <div class="title">CRM Solutions<span class="badge"><span></span></span></div>
    <div class="body">CRMs (Customer Relationship Management) can be complex and slow for employees to adopt. Accelerate your CRM adoption by selecting the right simple solution for your business.</div>
    <span class="btn">Read more ▸</span>
  </div>
</section>
<div class="abs dots"><i></i><i></i><i></i><i></i></div>

<h2 class="abs section-title heading" style="top:660px"><span class="a">Welcome to</span> <span class="b">Vale Lanternwick</span></h2>
<div class="abs rule" style="top:705px"></div>
<p class="abs lead" style="top:724px;left:170px;width:860px">Success in the cloud begins with a sound strategy. Start with a strong evaluation process. Then determine the right solution, proper implementation strategy and change management method. With the right transition you could recognize the benefits of the cloud:</p>

<article class="abs feature" style="left:158px">
  <div class="ring"><span>
    <svg width="90" height="90" viewBox="0 0 90 90" fill="none" stroke="#fff" stroke-width="7"><path d="M15 40a30 30 0 0 1 52-18"/><path d="M75 50a30 30 0 0 1-52 18"/><path d="M70 8v16H54" stroke-width="6"/><path d="M20 82V66h16" stroke-width="6"/><path d="M55 32c-2-4-6-5-10-5-6 0-10 3-10 8 0 10 20 6 20 16 0 5-4 8-10 8-5 0-9-2-11-6M45 20v50" stroke-width="6"/></svg>
  </span></div>
  <h3>Less infrastructure<br>and IT costs.</h3>
  <p>A cloud solution definitely means buying less hardware at your location. This also means less IT support. What is the best solution? Is a SaaS product right or do you need more customized solutions? What works for you?</p>
  <span class="btn">Read more</span>
</article>

<article class="abs feature" style="left:473px">
  <div class="ring"><span>
    <svg width="84" height="84" viewBox="0 0 84 84" fill="#fff"><path d="M4 4h28L22 14l12 12-8 8-12-12L4 32z"/><path d="M80 4v28L70 22 58 34l-8-8 12-12L52 4z"/><path d="M4 80V52l10 10 12-12 8 8-12 12 10 10z"/><path d="M80 80H52l10-10-12-12 8-8 12 12 10-10z"/></svg>
  </span></div>
  <h3>Scalability</h3>
  <p>Cloud computing allows your business to easily upscale or downscale your IT requirements without expensive changes to your existing IT system. What solutions offer the scalability for your organization? We can review and advise.</p>
  <span class="btn">Read more</span>
</article>

<article class="abs feature" style="left:788px">
  <div class="ring"><span>
    <svg width="90" height="90" viewBox="0 0 90 90" fill="#fff" stroke="#fff" stroke-width="5"><circle cx="45" cy="45" r="15" stroke="none"/><path d="M45 30V12M45 60v18M30 45H12M60 45h18M34 34 22 22M56 56l12 12M56 34l12-12M34 56 22 68"/><circle cx="45" cy="10" r="7" stroke="none"/><circle cx="45" cy="80" r="7" stroke="none"/><circle cx="10" cy="45" r="7" stroke="none"/><circle cx="80" cy="45" r="7" stroke="none"/><circle cx="20" cy="20" r="5" stroke="none"/><circle cx="70" cy="70" r="5" stroke="none"/><circle cx="70" cy="20" r="5" stroke="none"/><circle cx="20" cy="70" r="5" stroke="none"/></svg>
  </span></div>
  <h3>Increase workforce<br>collaboration</h3>
  <p>Make it easier for your remote employees to be part of the organization. Give more flexibility to your staff to work they way they live. How do your train and promote adoption? Our advisors can define a clear plan.</p>
  <span class="btn">Read more</span>
</article>

<section class="abs services">
  <h2 class="abs section-title heading" style="top:42px"><span class="a">What</span> <span class="b">we do</span></h2>
  <div class="abs rule" style="top:89px"></div>
  <p class="abs lead" style="top:110px;left:170px;width:860px">We challenge the status quo by providing unique insights, emerging strategies and proven best practices. Our unwavering focus is on customer satisfaction. Our services include:</p>

  <div class="abs service" style="left:162px;top:239px">
    <div class="icon"><svg width="54" height="54" viewBox="0 0 54 54"><path d="M27 12a12 12 0 0 0-7 22v5h14v-5a12 12 0 0 0-7-22z" fill="#fff"/><rect x="21" y="41" width="12" height="3" fill="var(--yellow)"/><rect x="22" y="46" width="10" height="3" fill="var(--yellow)"/><path d="M27 2v6M9 10l4 4M45 10l-4 4M2 24h6M46 24h6" stroke="var(--yellow)" stroke-width="3"/></svg></div>
    Strategy
  </div>
  <div class="abs service" style="left:339px;top:239px">
    <div class="icon"><svg width="60" height="54" viewBox="0 0 60 54"><path d="M16 42a12 12 0 0 1-1-24 16 16 0 0 1 30 2 11 11 0 0 1 1 22z" fill="var(--yellow)"/><circle cx="30" cy="32" r="11" fill="none" stroke="#fff" stroke-width="4"/><path d="M36 20l5 4-6 3z" fill="#fff"/></svg></div>
    Migration
  </div>
  <div class="abs service" style="left:512px;top:239px">
    <div class="icon"><svg width="54" height="54" viewBox="0 0 54 54"><circle cx="20" cy="33" r="10" fill="none" stroke="#fff" stroke-width="6" stroke-dasharray="4 3"/><circle cx="20" cy="33" r="5" fill="#fff"/><circle cx="37" cy="17" r="8" fill="none" stroke="var(--yellow)" stroke-width="5" stroke-dasharray="3 3"/><circle cx="37" cy="17" r="4" fill="var(--yellow)"/></svg></div>
    Implementation
  </div>
  <div class="abs service" style="left:695px;top:239px">
    <div class="icon"><svg width="54" height="54" viewBox="0 0 54 54" fill="none" stroke-width="6"><path d="M10 26a16 16 0 0 1 26-12" stroke="var(--yellow)"/><path d="M32 6l10 8-12 4z" fill="var(--yellow)" stroke="none"/><path d="M44 28a16 16 0 0 1-26 12" stroke="#fff"/><path d="M22 48l-10-8 12-4z" fill="#fff" stroke="none"/></svg></div>
    Integration
  </div>
  <div class="abs service" style="left:868px;top:239px">
    <div class="icon"><svg width="60" height="54" viewBox="0 0 60 54"><path d="M6 27c0-12 8-20 22-20h20l8 8H28c-8 0-12 5-12 12z" fill="var(--yellow)"/><path d="M54 27c0 12-8 20-22 20H12l-8-8h28c8 0 12-5 12-12z" fill="var(--yellow)"/><path d="M18 19l8 8-8 8M28 19l8 8-8 8M38 19l8 8-8 8" fill="none" stroke="#fff" stroke-width="4"/></svg></div>
    Adoption and<br>change management
  </div>
  <span class="btn">Contact us</span>
</section>
<div class="abs notch"></div>

<h2 class="abs section-title heading" style="top:2004px"><span class="a">About</span> <span class="b">us</span></h2>
<div class="abs rule" style="top:2050px"></div>
<p class="abs lead" style="top:2080px;left:170px;width:860px">Rowan Pell and Ines Marlow have combined their expertise and international team to offer quality advice on cloud strategies. Our objective is to provide guidance, thought leadership and strategic support to make the right decisions as you move your company forward.</p>

<article class="abs member" style="left:268px">
  <div class="avatar a1" role="img" aria-label="Portrait photo of Rowan Pell"></div>
  <h4>Rowan Pell - Position</h4>
  <p>IT services consultant and infrastructure architect with a strong background in a wide range of IT infrastructure and application development exposure. Most effective designing and managing infrastructure and IT services in start-ups, high tech companies, and companies undergoing growth and structural change.</p>
  <span class="pill">Read more</span>
  <div class="social-dots"><i></i><i></i><i></i></div>
</article>

<article class="abs member" style="left:648px">
  <div class="avatar a2" role="img" aria-label="Portrait photo of Ines Marlow"></div>
  <h4>Ines Marlow - Position</h4>
  <p>Deep experienced in delivering a wide variety of IT business applications on time and within budget from very large to very small companies. Seeing hyper-growth operations as well as streamlining steady business practices in the financial services, communications, media, retail industries, I have managed implementations and daily operations.</p>
  <span class="pill">Read more</span>
  <div class="social-dots"><i></i><i></i><i></i></div>
</article>

<footer class="abs footer">
  <h5 style="left:162px">Navigation</h5>
  <ul style="left:162px"><li>Cloud Services</li><li>Cloud Advisory</li><li>Cloud Technology</li><li>Case Studies</li></ul>
  <h5 style="left:388px">Useful Info</h5>
  <ul style="left:388px"><li>FAQ</li><li>Sitemap</li><li>Terms &amp; Agreement</li><li>Privacy Policy</li></ul>
  <h5 style="left:612px">Contact us</h5>
  <div class="contact-list">
    <div>✉&nbsp; hello@valelanternwick.example</div>
    <div>☎&nbsp; 02-5550-014</div>
  </div>
  <div class="social-dots"><i></i><i></i><i></i></div>
  <h5 style="left:852px">Quick Message</h5>
  <div class="field" style="top:119px;height:30px">Firstname</div>
  <div class="field" style="top:160px;height:30px">Email address</div>
  <div class="field" style="top:204px;height:88px">Message</div>
  <div class="submit">SUBMIT</div>
</footer>
<div class="abs copyright">Copyright © 2014 Vale Lanternwick</div>

</body>
</html>
```